Biz Cards for Lumivale Associates

Lumivale Associates is seeking a single-sided business card that is more visually-appealing than our current design (see attached).

Notes:
- Our colors are blue & teal.
- Our tag line must be large enough to be easily read
- We don't necessarily need our address included (that's just the biz office)
- We'd like to add our email address: Lumivale512@brindlemail.net

Thanks!

Industry/Entity Type

Business

Contact Information for Business Card

Standard size
PSD file required w/ text on its own layer

Colors
86cfc6
3277b5

```html
<!DOCTYPE html>
<html lang="en">
<head>
<meta charset="utf-8">
<title>Lumivale Associates – Business Card</title>
<link href="https://fonts.googleapis.com/css2?family=Arimo:ital,wght@0,400;0,700;1,400&display=swap" rel="stylesheet">
<style>
  :root {
    --page-bg: #e4e2df;
    --frost: #e9e8e6;
    --frost-shade: #d3d2d0;
    --text-light: #ecebea;
    --text-soft: #d9d8d6;
    --brand-blue: #3277b5;
    --brand-teal: #86cfc6;
    --curve-blue: #1f4f8f;
    --logo-ink: #1a1a1a;
  }
  html, body {
    margin: 0;
    width: 1200px;
    height: 970px;
    overflow: hidden;
    background: var(--page-bg);
  }
  .business-card {
    position: absolute;
    left: 100px;
    top: 200px;
    width: 1000px;
    height: 570px;
    border-radius: 34px;
    overflow: hidden;
    background: linear-gradient(135deg, var(--frost) 0%, var(--frost-shade) 100%);
    box-shadow: 0 10px 30px rgba(0,0,0,0.18);
    font-family: "Arimo", Arial, sans-serif;
  }
  .card-shapes {
    position: absolute;
    inset: 0;
  }
  .contact-panel {
    position: absolute;
    left: 48px;
    top: 78px;
    color: var(--text-light);
  }
  .person-name {
    font-size: 34px;
    margin: 0;
    font-weight: 400;
    letter-spacing: 0.2px;
  }
  .person-role {
    font-size: 26px;
    margin: 4px 0 0 3px;
    color: var(--text-soft);
  }
  .office-address {
    font-style: normal;
    font-size: 26px;
    line-height: 34px;
    margin: 50px 0 0 3px;
    color: var(--text-soft);
  }
  .contact-list {
    list-style: none;
    padding: 0;
    margin: 38px 0 0 0;
    font-size: 26px;
    line-height: 34px;
    color: var(--text-soft);
  }
  .contact-list li {
    display: flex;
    align-items: center;
    gap: 10px;
  }
  .contact-icon {
    width: 28px;
    height: 28px;
    flex: none;
  }
  .web-address {
    margin: 36px 0 0 0;
    font-size: 26px;
    color: var(--brand-blue);
    opacity: 0.85;
  }
  .side-dot {
    position: absolute;
    left: -22px;
    top: 80px;
    width: 44px;
    height: 60px;
    border-radius: 50%;
    background: var(--brand-blue);
    opacity: 0.75;
  }
  .brand-block {
    position: absolute;
    left: 520px;
    top: 180px;
    width: 460px;
    text-align: center;
    color: var(--logo-ink);
  }
  .brand-mark {
    display: block;
    width: 100px;
    height: 100px;
    margin: 0 auto 16px;
    border-radius: 50%;
    background: var(--brand-teal);
  }
  .brand-name {
    font-size: 40px;
    font-weight: 700;
    margin: 0;
    line-height: 1.1;
    white-space: nowrap;
  }
  .brand-tagline {
    font-size: 16px;
    margin: 12px 0 0 0;
    color: var(--curve-blue);
    font-style: italic;
    white-space: nowrap;
  }
</style>
</head>
<body>
  <div class="business-card">
    <svg class="card-shapes" width="1000" height="570" viewBox="0 0 1000 570">
      <defs>
        <linearGradient id="darkPanel" x1="0" y1="0" x2="1" y2="1">
          <stop offset="0" stop-color="#2f2f32"/>
          <stop offset="1" stop-color="#141416"/>
        </linearGradient>
      </defs>
      <path d="M0 0 H520 Q420 285 520 570 H0 Z" fill="url(#darkPanel)"/>
      <path d="M524 0 Q428 285 524 570" fill="none" stroke="#1f4f8f" stroke-width="5"/>
      <path d="M531 0 Q438 285 531 570" fill="none" stroke="#bfc3c8" stroke-width="2" opacity="0.7"/>
    </svg>

    <span class="side-dot"></span>

    <section class="contact-panel">
      <h1 class="person-name">Marisol Keane, RN</h1>
      <p class="person-role">Mental Health Therapist</p>
      <address class="office-address">
        4127 Hollin Ave<br>
        Suite 310<br>
        Brookfield, OH&nbsp; 44320
      </address>
      <ul class="contact-list">
        <li>
          <svg class="contact-icon" viewBox="0 0 28 28"><circle cx="14" cy="14" r="12.5" fill="none" stroke="#3277b5" stroke-width="1.5"/><path d="M8 11 Q14 6 20 11 L18 13 L16 11.5 L12 11.5 L10 13 Z M9 15 H19 V20 H9 Z" fill="#3277b5"/></svg>
          (855) LUMI-VAL
        </li>
        <li>
          <svg class="contact-icon" viewBox="0 0 28 28"><circle cx="14" cy="14" r="12.5" fill="none" stroke="#3277b5" stroke-width="1.5"/><rect x="9" y="7" width="10" height="5" fill="#3277b5"/><rect x="7" y="12" width="14" height="6" rx="1" fill="#3277b5"/><rect x="9" y="16" width="10" height="5" fill="#3277b5"/></svg>
          (330) 555-0184
        </li>
        <li>
          <svg class="contact-icon" viewBox="0 0 28 28"><circle cx="14" cy="14" r="12.5" fill="none" stroke="#3277b5" stroke-width="1.5"/><rect x="7.5" y="9.5" width="13" height="9" fill="#3277b5"/><path d="M7.5 9.5 L14 15 L20.5 9.5" fill="none" stroke="#1c1c1e" stroke-width="1.2"/></svg>
          Lumivale512@brindlemail.net
        </li>
      </ul>
      <p class="web-address">Lumivale.net</p>
    </section>

    <section class="brand-block">
      <span class="brand-mark"></span>
      <p class="brand-name">Lumivale Associates</p>
      <p class="brand-tagline">Calm Minds. Kind Support. Lasting Wellness.</p>
    </section>
  </div>
</body>
</html>
```